Business Card for TQM

We need a Corporate style business card for a new Industrial recycling company based in Australia. We recycle industrial products from Mining companies, power stations and other large industry all around the country.

We want the card to represent a modern, innovative professional company that is an industry leader.

We want the card to be double sided. I think with the logo centred by itself on one side and the text displayed with all our details on the other side.

(or you could put the persons name with the job title on the side with the logo?? I'll leave that up to your creative sides)

Open to how you divide and place the information on the one side of the card.

I think the persons name and the title should have its own place. The rest of the information can be placed as you think is best and then I will provide feedback as to what I think works best.

I have attached the logo file so you can add that to the one side. Whether you use it in a smaller form on the second side too is an option but I'll leave that up to you initially?

Information required on the card is as follows

Darren Pollock
Director

0428 917 306

darren@tqmv.com.au

Po Box 582
Brindle ACT 2611

www.tqmv.com.au

ACN 273 581 926 (This can be in very small print and can be in the bottom corner of the card or somewhere not very prominent
Updates

Wanted to thank everyone for their submissions. 

We were really torn on about 5 designs in the end.

We decided to go with the first one we liked.

We have another company that is going to need logo and business card design in the coming weeks.

I will save your designer ID's so I can invite you all to that project. too!

Thanks again and all the best

Darren

Target Market(s)

Corporate and medium to large business clients

Industry/Entity Type

Industrial

```html
<!DOCTYPE html>
<html lang="en">
<head>
<meta charset="utf-8">
<title>Tasman Quality Materials – Business Card</title>
<link href="https://fonts.googleapis.com/css2?family=Quicksand:wght@500;600;700&display=swap" rel="stylesheet">
<style>
  :root {
    --bg: #e4e4e6;
    --card: #f7f7f5;
    --green: #6abd2c;
    --green-dark: #4f9a1c;
    --blue: #3d7db5;
    --ink: #3a3a3a;
    --muted: #8a8a8a;
  }
  * { margin: 0; padding: 0; box-sizing: border-box; }
  html, body { width: 1200px; height: 750px; overflow: hidden; }
  body {
    background: var(--bg);
    font-family: "Quicksand", sans-serif;
    color: var(--ink);
    position: relative;
  }
  .card {
    position: absolute;
    top: 232px;
    width: 500px;
    height: 286px;
    border-radius: 22px;
    background: var(--card);
    overflow: hidden;
    box-shadow: 0 6px 18px rgba(0,0,0,0.12);
  }
  .card--front { left: 70px; }
  .card--back { left: 630px; }

  /* Front side */
  .band { position: absolute; left: 0; width: 100%; background: var(--green); }
  .band--top { top: 0; height: 62px; }
  .band--bottom { bottom: 0; height: 74px; }
  .front-brand {
    position: absolute; top: 62px; bottom: 74px; left: 0; right: 0;
    display: flex; align-items: center; justify-content: center; gap: 16px;
  }
  .brand-mark {
    width: 44px; height: 44px; border-radius: 50%; background: var(--green);
    flex: none;
  }
  .brand-name {
    font-weight: 700; color: var(--ink);
    font-size: 21px; line-height: 1.05; letter-spacing: 0.04em; text-transform: uppercase;
  }

  /* Back side */
  .swoosh { position: absolute; top: 0; left: 0; width: 500px; height: 110px; }
  .back-brand {
    position: absolute; left: 34px; top: 118px; width: 190px;
    display: flex; flex-direction: column; align-items: center; gap: 10px;
  }
  .back-brand .brand-mark { width: 58px; height: 58px; }
  .back-brand .brand-name { font-size: 17px; text-align: center; }
  .acn { font-size: 7px; color: var(--muted); font-weight: 600; letter-spacing: 0.05em; }

  .divider {
    position: absolute; left: 244px; top: 96px; width: 2px; height: 122px; background: var(--green);
  }
  .contact { position: absolute; left: 260px; top: 90px; }
  .person-name { color: var(--green-dark); font-weight: 600; font-size: 17px; line-height: 1; }
  .person-title { color: var(--ink); font-size: 9px; font-weight: 600; margin-bottom: 6px; }
  .contact-list { list-style: none; }
  .contact-item {
    display: flex; align-items: flex-start; gap: 8px;
    color: var(--blue); font-size: 14px; font-weight: 500; line-height: 1.35;
  }
  .contact-item svg { width: 13px; height: 13px; margin-top: 3px; flex: none; fill: var(--green-dark); }
  .contact-item .address-line2 { color: var(--ink); display: block; }
</style>
</head>
<body>

  <section class="card card--front" aria-label="Business card front">
    <div class="band band--top"></div>
    <div class="front-brand">
      <span class="brand-mark"></span>
      <span class="brand-name">Tasman Quality<br>Materials</span>
    </div>
    <div class="band band--bottom"></div>
  </section>

  <section class="card card--back" aria-label="Business card back">
    <svg class="swoosh" viewBox="0 0 500 110" preserveAspectRatio="none" aria-hidden="true">
      <path d="M0 0 H500 V58 C400 20 250 30 150 70 C90 92 40 100 0 104 Z" fill="var(--green)"/>
    </svg>

    <div class="back-brand">
      <span class="brand-mark"></span>
      <span class="brand-name">Tasman Quality<br>Materials</span>
      <span class="acn">ACN 273 581 926</span>
    </div>

    <div class="divider"></div>

    <div class="contact">
      <p class="person-name">Darren Pollock</p>
      <p class="person-title">director</p>
      <ul class="contact-list">
        <li class="contact-item">
          <svg viewBox="0 0 16 16" aria-hidden="true"><path d="M2 5c0-2 2-3 6-3s6 1 6 3v1h-3V5H5v1H2zM4 7h8l2 7H2z"/></svg>
          <span>0428 917 306</span>
        </li>
        <li class="contact-item">
          <svg viewBox="0 0 16 16" aria-hidden="true"><circle cx="8" cy="8" r="7"/><rect x="4" y="5" width="8" height="6" fill="#f7f7f5"/></svg>
          <span>darren@tqmv.com.au</span>
        </li>
        <li class="contact-item">
          <svg viewBox="0 0 16 16" aria-hidden="true"><path d="M2 2l12 5-5 2-2 5z"/></svg>
          <span>www.tqmv.com.au</span>
        </li>
        <li class="contact-item">
          <svg viewBox="0 0 16 16" aria-hidden="true"><path d="M8 1l7 7h-2v7H9v-4H7v4H3V8H1z"/></svg>
          <span>Po Box 582<span class="address-line2">Brindle ACT 2611</span></span>
        </li>
      </ul>
    </div>
  </section>

</body>
</html>
```